Label (re) design of premium yacht nanotechnology care

We need a (re) design of a label for our premium yacht care product line. We developed lubrication, cleaning and nanotechnology protection products for the retail market. We have an existing brand which needs a modernization and upgrade. Our label and logo needs bright colors, should be practical to use and should respect the elements described in the attached document. Sun, see, yacht pleasure and professional nanotechnology should be put into one colorful and fun label.

Target Market(s)

Yacht cleaning/protection/antifouling

Industry/Entity Type

Retail

Font styles to use
Sans Serif

Requirements
Must have
• Modern, bright design that looks premium
Nice to have
• Out of the box
Should not have
• Outdated design

```html
<!DOCTYPE html>
<html lang="en">
<head>
<meta charset="utf-8">
<title>Nano Teak Protector – Label</title>
<link rel="stylesheet" href="https://fonts.googleapis.com/css2?family=Plus+Jakarta+Sans:wght@400;500;600;700;800&display=swap">
<style>
  :root {
    --navy: #1a1c3a;
    --white: #ffffff;
    --gold-light: #f4ecd2;
    --gold: #c9b47f;
    --gold-dark: #a8915a;
    --bg-top: #a9bbd0;
    --bg-mid: #d9e1ea;
    --wood-dark: #7a3f1c;
    --wood: #a8612f;
    --wood-light: #c98a55;
    --rule: #cfd2e0;
  }
  * { box-sizing: border-box; margin: 0; padding: 0; }
  html, body { width: 1200px; height: 1144px; overflow: hidden; }
  body {
    font-family: "Plus Jakarta Sans", sans-serif;
    background: radial-gradient(ellipse at 50% 60%, var(--bg-mid) 0%, var(--bg-top) 80%);
    position: relative;
    color: var(--navy);
  }

  /* ---------- Front label ---------- */
  .front-label {
    position: absolute; left: 34px; top: 278px;
    width: 560px; height: 590px;
    background: var(--white);
    overflow: hidden;
  }
  .brand-band {
    height: 120px; background: var(--navy);
    display: flex; align-items: center; justify-content: center;
  }
  .brand-name {
    color: var(--white); font-weight: 700; font-size: 30px; letter-spacing: -0.5px;
    display: flex; align-items: center; gap: 12px;
  }
  .brand-dot { width: 14px; height: 14px; border-radius: 50%; background: var(--gold); }

  .title-box {
    position: absolute; left: 86px; top: 212px; width: 388px; height: 126px;
    border: 2px solid var(--gold); border-radius: 14px; overflow: hidden;
    background: var(--white);
  }
  .title-en, .title-nl {
    height: 50%; display: flex; align-items: center; justify-content: center;
    font-weight: 800; font-size: 32px; letter-spacing: -1.6px; color: var(--navy);
  }
  .title-en { background: linear-gradient(180deg, var(--gold-light) 0%, #e6d9ae 55%, var(--gold) 100%); }
  .title-nl { border-top: 2px solid var(--gold-dark); }

  .steps {
    position: absolute; left: 100px; top: 362px; width: 360px;
    display: flex; justify-content: space-between;
  }
  .step { width: 84px; text-align: center; font-size: 13px; letter-spacing: -0.4px; }
  .step svg { display: block; margin: 0 auto 6px; width: 50px; height: 48px; }

  .wood-rule { position: absolute; left: 0; top: 483px; width: 100%; height: 7px; background: var(--navy); }
  .wood-photo {
    position: absolute; left: 0; top: 490px; width: 100%; height: 100px;
    background: linear-gradient(100deg, var(--wood-dark) 0%, var(--wood) 30%, var(--wood-light) 55%, var(--wood) 78%, var(--wood-dark) 100%);
  }
  .volume {
    position: absolute; left: 0; top: 530px; width: 100%; text-align: center;
    font-size: 15px; color: var(--navy); letter-spacing: -0.3px;
  }

  /* ---------- Back label ---------- */
  .back-label {
    position: absolute; left: 606px; top: 278px;
    width: 560px; height: 590px;
    background: var(--navy); color: var(--white);
    padding: 30px 30px 26px;
  }
  .section-head {
    font-weight: 600; font-size: 11px; padding-bottom: 5px;
    border-bottom: 1px solid var(--rule); margin-bottom: 6px;
  }
  .section-head.small { font-size: 8px; }
  .cols { display: grid; grid-template-columns: 1fr 1fr; column-gap: 8px; }
  .desc { font-size: 10.5px; line-height: 1.36; text-align: justify; letter-spacing: -0.2px; }
  .desc.nl { letter-spacing: -0.3px; }
  .col-left, .col-right { display: flex; flex-direction: column; }
  .checklist { list-style: none; font-size: 9px; line-height: 1.45; letter-spacing: -0.3px; margin-bottom: 6px; }
  .checklist.small { font-size: 7px; line-height: 1.5; }
  .checklist li { position: relative; padding-left: 11px; }
  .checklist li::before {
    content: ""; position: absolute; left: 1px; top: 0.45em;
    width: 5px; height: 2.5px; border-left: 1.3px solid var(--white); border-bottom: 1.3px solid var(--white);
    transform: rotate(-45deg);
  }
  .block-gap { margin-top: 10px; }
  .batch {
    align-self: flex-end; margin-top: -6px;
    border: 1px solid var(--white); border-radius: 4px;
    font-size: 8px; font-weight: 600; padding: 2px 12px;
  }
  .web {
    align-self: center; margin-top: 6px;
    border: 1px solid var(--white); border-radius: 4px;
    font-size: 7.5px; font-weight: 600; padding: 2px 14px;
  }
  .company { font-size: 7px; margin: 12px 0 0 14px; line-height: 1.6; }
  .company b { font-weight: 700; font-size: 7.5px; }
  .hazards { display: flex; gap: 6px; margin: 14px 0 0 14px; flex-wrap: wrap; width: 64px; justify-content: center; }
  .hazards svg { width: 28px; height: 26px; }
</style>
</head>
<body>

<section class="front-label">
  <div class="brand-band">
    <div class="brand-name"><span class="brand-dot"></span>Marlow Harbour by Kestrel</div>
  </div>

  <div class="title-box">
    <div class="title-en">Nano Teak Protector</div>
    <div class="title-nl">Nano Teak Beschermer</div>
  </div>

  <div class="steps">
    <div class="step">
      <svg viewBox="0 0 50 48" fill="none" stroke="#1a1c3a" stroke-width="2.4" stroke-linecap="round">
        <path d="M14 4c-3 3 3 5 0 9M22 4c-3 3 3 5 0 9M30 4c-3 3 3 5 0 9M38 4c-3 3 3 5 0 9"/>
        <rect x="6" y="18" width="38" height="5" fill="#1a1c3a"/>
        <path d="M10 27h30l-4 16H14z" fill="#1a1c3a"/>
        <path d="M18 29v12M25 29v12M32 29v12" stroke="#fff" stroke-width="2"/>
      </svg>
      Pre wash
    </div>
    <div class="step">
      <svg viewBox="0 0 50 48" fill="#1a1c3a">
        <circle cx="18" cy="28" r="13"/><circle cx="31" cy="35" r="8" stroke="#fff" stroke-width="2"/>
        <circle cx="34" cy="20" r="5"/><path d="M42 4l2 5 5 2-5 2-2 5-2-5-5-2 5-2z"/>
      </svg>
      Wash
    </div>
    <div class="step">
      <svg viewBox="0 0 50 48" fill="#1a1c3a">
        <rect x="22" y="2" width="5" height="5"/><rect x="20" y="10" width="10" height="34" rx="2"/>
        <rect x="8" y="22" width="11" height="22" rx="2"/><rect x="31" y="30" width="9" height="14" rx="2"/>
        <circle cx="40" cy="14" r="1.6"/><circle cx="44" cy="22" r="1.6"/>
      </svg>
      Shampoo
    </div>
    <div class="step">
      <svg viewBox="0 0 50 48" fill="none">
        <path d="M25 2l19 6v14c0 12-8 20-19 24C14 42 6 34 6 22V8z" fill="#1a1c3a"/>
        <circle cx="25" cy="22" r="9" stroke="#fff" stroke-width="2.4"/>
        <path d="M25 17v10M20 22h10" stroke="#fff" stroke-width="2.4"/>
      </svg>
      Protect
    </div>
  </div>

  <div class="wood-rule"></div>
  <div class="wood-photo" role="img" aria-label="Close-up photo of oiled teak deck with water beading on the surface"></div>
  <div class="volume">1 ltr</div>
</section>

<section class="back-label">
  <div class="section-head">Product Description</div>
  <div class="cols">
    <p class="desc">Nano Teak Protector Clear is a transparent and high-quality protective for teak. It is based on nano-technology. Prevents pollution. Consequetly the growth of algae will be reduced drastically. It impregnates and preserves the wood, which prevents aging and makes the top layer water- and grease proof. It won't make the teak glossy and it won't change the colour. It is ideal for maintaining new and grey aged teak. Does not affect the kit between the teak and won't make the deck slippery.</p>
    <p class="desc nl">Nano Teak Beschermer Naturel is een transparant en hoogwaardig beschermingsmiddel voor teak. Het is gebaseerd op Nanotechnologie. Beschermt langdurig tegen het aanhechten van vervuiling. Voorkomt vervuiling, zodat de aangroei van algen drastisch wordt verminderd. Verduurzaamt en impregneert het hout, waardoor veroudering ervan wordt voorkomen. Bovendien wordt de bovenlaag water- en vetafstotend. Laat het oppervlak niet glimmen en geeft geen kleurverandering. Ideaal voor het in stand houden van nieuw en vergrijsd teak. Tast kitverbinding- en niet aan en het teakdek wordt niet glad.</p>
  </div>

  <div class="cols block-gap">
    <div class="col-left">
      <div class="section-head" style="font-size:9px">Instruction for use :</div>
      <ul class="checklist">
        <li>Shake well before use.</li>
        <li>Make sure that the surface to be treated is clean and dry.</li>
        <li>Apply with a brush or a clean cloth.</li>
        <li>Let the product soak in for a few minutes and finally wipe off with a dry clean cloth any excess product.</li>
        <li>If necessary, repeat the treatment.</li>
      </ul>
      <div class="section-head" style="font-size:9px">Danger :</div>
      <ul class="checklist">
        <li>H225 Highly flammable liquid and vapour.</li>
        <li>H317 May cause an allergic skin reaction.</li>
        <li>P210 Keep away from heat/sparks/open flames/hot surfaces.</li>
        <li>P261 Avoid breathing dust/fume/gas/mist/vapours/spray.</li>
        <li>P280 Wear protective gloves/protective clothing/eye protection/face protection.</li>
      </ul>
      <div class="section-head" style="font-size:9px">In case of fire</div>
      <ul class="checklist">
        <li>Use foam for extinction.</li>
        <li>P403 + P235 Store in a well-ventilated place.</li>
        <li>Keep Cool.</li>
        <li>P501 Dispose of contents/container tochemical waste collection.</li>
      </ul>
      <div class="batch">Batch No : 1029938</div>
    </div>

    <div class="col-right">
      <div class="section-head small">Gebruiksaanwijzing:</div>
      <ul class="checklist small">
        <li>Goed schudden voor gebruik.</li>
        <li>Hette behandelen oppervlak dient schoon endroog tezijn.</li>
        <li>Breng het product met een kwast of doek aan.</li>
        <li>Laat het product enkele minuten intrekken. Wrijf het met een nieuwe droge schone doek goed uit om overtollig product te verwijderen.</li>
        <li>Indien nodig de behandeling herhalen.</li>
      </ul>
      <div class="section-head small">Gevaar :</div>
      <ul class="checklist small">
        <li>H225 Licht ontvlambare vloeistof en damp.</li>
        <li>H317 Kan een allergische huidreactie veroorzaken.</li>
        <li>P210 Verwijderd houden van warmte/vonken/open vuur/hete oppervlakken.</li>
        <li>P261 Inademing van stof/rook/gas/nevel/damp/spuitnevel vermijden.</li>
        <li>P280 Beschermende handschoenen/beschermende kleding/oogbescherming/ gelaatsbescherming dragen.</li>
      </ul>
      <div class="web">www.marlowharbour.com</div>
      <p class="company"><b>Address:</b> MH Marine B.V. P.O. Box 4120, 3000 AB Harbourtown (NL)<br><b>Developed and produced by:</b> KESTREL LABORATORIES</p>
      <div class="hazards">
        <svg viewBox="0 0 28 26"><path d="M14 1l13 24H1z" fill="#f4ecd2" stroke="#c9b47f"/><path d="M14 10c3 3 4 6 2 10h-4c-2-3 0-6 2-10z" fill="#1a1c3a"/></svg>
        <svg viewBox="0 0 28 26"><path d="M14 1l13 24H1z" fill="#f4ecd2" stroke="#c9b47f"/><path d="M14 9v9" stroke="#1a1c3a" stroke-width="2.6"/><circle cx="14" cy="21.5" r="1.5" fill="#1a1c3a"/></svg>
        <svg viewBox="0 0 28 26"><circle cx="14" cy="13" r="12" fill="#f4ecd2" stroke="#c9b47f"/><path d="M7 14h12" stroke="#1a1c3a" stroke-width="3"/><path d="M6 6l16 14" stroke="#1a1c3a" stroke-width="2"/></svg>
      </div>
    </div>
  </div>
</section>

</body>
</html>
```